Christmas card for printing and emailing

We are an international translation service provider based in Barcelona and would like to send a personalized Season's Greetings e-mail to our contacts. The design should take into account our activity (translation services) and perhaps play with our logo.
the size should be postcard size in order to fit in a standard DIN C6 = 114 x 162 mm envelope. There will be no text on the card, only an image, the text will go on the other side of the card. The card will have an local version (ES) with the ES logo and an international version the the EN logo.
The design should take into account our corporative colours (see our website www.valdoraling.es) and the seriousness of our corporative image.

We attach our logo and our company style guide.

Target Market(s)

Target: Companies and institutions, executives like export managers, marketing managers, top level secretaries

Industry/Entity Type

Translation Services

Requirements
Must have
• Our logo in it. Refer to Season's greetings. Our corporate colours
Nice to have
• Modern design, perhaps 3D, international, techy taste
Should not have
• Please avoid: very colourful designs with typical Christmas stationery. Old fashion style designs as our company is a technologic one.

```html
<!DOCTYPE html>
<html lang="en">
<head>
<meta charset="utf-8">
<title>Season's Greetings Postcards</title>
<link rel="stylesheet" href="https://fonts.googleapis.com/css2?family=Dancing+Script:wght@500;600&display=swap">
<style>
  :root {
    --navy: #1d4f82;
    --slate: #7c99b5;
    --photo-deep: #1e5a72;
    --photo-light: #9fd6f2;
    --ice: #dce3ec;
    --rule: #b9c6d5;
    --white: #ffffff;
  }
  * { margin: 0; padding: 0; box-sizing: border-box; }
  html, body { width: 1200px; height: 1000px; overflow: hidden; background: var(--white); }
  .canvas { position: relative; width: 1200px; height: 1000px; }

  .card-front { position: absolute; width: 458px; height: 322px; }
  .card-front svg { display: block; }
  .front-one { left: 117px; top: 145px; }
  .front-two { left: 117px; top: 547px; }

  .brand-box {
    position: absolute; left: 20px; top: 248px; width: 153px; height: 62px;
    background: var(--white);
    display: flex; align-items: center; justify-content: center; gap: 7px;
    padding: 0 12px;
  }
  .brand-mark { flex: 0 0 auto; width: 12px; height: 12px; background: var(--navy); }
  .brand-name {
    font-family: "Dancing Script", cursive; font-weight: 600;
    font-size: 17px; line-height: 1; color: var(--navy); white-space: nowrap;
  }

  .card-back { position: absolute; border: 3px solid var(--navy); background: var(--white); overflow: hidden; }
  .back-one { left: 641px; top: 155px; width: 431px; height: 303px; }
  .back-two { left: 627px; top: 546px; width: 460px; height: 324px; }
  .back-two .back-field {
    position: absolute; left: 8px; top: 8px; right: 9px; bottom: 8px; background: var(--ice);
  }

  .divider { position: absolute; }
  .back-one .divider { left: 213px; top: 25px; width: 1px; height: 253px; background: var(--rule); }
  .back-two .divider { left: 227px; top: 34px; width: 3px; height: 254px; background: var(--navy); }

  .greeting-verse {
    position: absolute; text-align: center;
    font-family: "Dancing Script", cursive; font-weight: 600;
    font-size: 16px; line-height: 27px; color: var(--navy);
  }
  .back-one .greeting-verse { left: 8px; top: 70px; width: 200px; }
  .back-two .greeting-verse { left: 22px; top: 78px; width: 200px; }

  .greeting-title {
    position: absolute;
    font-family: "Dancing Script", cursive; font-weight: 600;
    font-size: 29px; line-height: 1.2; color: var(--navy); white-space: nowrap;
  }
  .back-one .greeting-title { left: 229px; top: 18px; }
  .back-two .greeting-title { left: 243px; top: 26px; }

  .address-lines {
    position: absolute;
    font-family: "Dancing Script", cursive; font-weight: 600;
    font-size: 26px; line-height: 42px; color: var(--navy); white-space: nowrap;
  }
  .back-one .address-lines { left: 233px; top: 112px; }
  .back-two .address-lines { left: 247px; top: 122px; }
</style>
</head>
<body>
<main class="canvas">

  <section class="card-front front-one">
    <svg width="458" height="322" viewBox="0 0 458 322">
      <defs>
        <linearGradient id="photoTone" x1="0" y1="1" x2="1" y2="0">
          <stop offset="0" stop-color="#163f58"/>
          <stop offset="0.45" stop-color="#1e5a72"/>
          <stop offset="0.75" stop-color="#9fd6f2"/>
          <stop offset="1" stop-color="#d8e3ea"/>
        </linearGradient>
      </defs>
      <rect width="458" height="322" fill="var(--navy)"/>
      <polygon points="30,0 195,0 195,100 0,140 0,95" fill="var(--slate)"/>
      <polygon role="img" aria-label="Photo of a keyboard with a large Translate key and a hand pressing a Translate button among language names"
               points="0,140 195,100 195,0 320,0 458,322 0,322" fill="url(#photoTone)"/>
    </svg>
    <div class="brand-box"><span class="brand-mark"></span><span class="brand-name">VALDORALING</span></div>
  </section>

  <section class="card-back back-one">
    <div class="divider"></div>
    <p class="greeting-verse">May all that is beautiful,<br>meaningful and brings<br>you joy,yours<br>this holiday season<br>&amp; throughout the coming your!</p>
    <h2 class="greeting-title">Marry christmas</h2>
    <p class="address-lines">To....................<br>From.................</p>
  </section>

  <section class="card-front front-two">
    <svg width="458" height="322" viewBox="0 0 458 322">
      <defs>
        <linearGradient id="photoToneTwo" x1="0" y1="1" x2="1" y2="0">
          <stop offset="0" stop-color="#163f58"/>
          <stop offset="0.45" stop-color="#1e5a72"/>
          <stop offset="0.75" stop-color="#9fd6f2"/>
          <stop offset="1" stop-color="#d8e3ea"/>
        </linearGradient>
      </defs>
      <rect width="458" height="322" fill="var(--navy)"/>
      <polygon points="30,0 195,0 195,100 0,140 0,95" fill="var(--slate)"/>
      <polygon role="img" aria-label="Photo of a keyboard with a large Translate key and a hand pressing a Translate button among language names"
               points="0,140 195,100 195,0 320,0 458,322 0,322" fill="url(#photoToneTwo)"/>
    </svg>
    <div class="brand-box"><span class="brand-mark"></span><span class="brand-name">VALDORALING</span></div>
  </section>

  <section class="card-back back-two">
    <div class="back-field"></div>
    <div class="divider"></div>
    <p class="greeting-verse">May all that is beautiful,<br>meaningful and brings<br>you joy,yours<br>this holiday season<br>&amp; throughout the coming your!</p>
    <h2 class="greeting-title">Marry christmas</h2>
    <p class="address-lines">To....................<br>From.................</p>
  </section>

</main>
</body>
</html>
```